Graphic Icon Set of 35 Icons

We are looking for a set of 35 graphic icons that we can use in all of our materials, from our new content website (under design), our PowerPoint presentations, our white papers, etc.
We prefer thin and elegant icons, but we are open to any style a designer might come up with, including multi-color or monochromatic, etc. Simpler is better than complex. We prefer a very clean design without the "noise" of really "busy" graphics. We specifically do not want any 3D graphics or graphics with shading or shine. We prefer a flat design.
We are looking for designer submissions that show an example of just three of the graphic icons: an icon that represents "Valuation" - how to value a business, an icon that represents "Advisory" - consulting with businesses, and an icon that represents a "Survey" - a reader survey. Please submit all three design in one submission in one view to make it easier for us to sort through the submissions.
We will then pick a winner and in order to get paid the full amount, you will need to design and deliver the rest of the set of 35 icons.
We are attaching a list of the 35 graphic icons we will want to be delivered by the winner in high-res, tightly-trimmed EPS, JPEG, and PNG file formats.
We are attaching a brand guidelines PDF with the description of our fonts, colors, logo, and images. We are also attaching an EPS of our logo.

```html
<!DOCTYPE html>
<html lang="en">
<head>
<meta charset="utf-8">
<title>Keenridge Growth Partners – Icon Set</title>
<link href="https://fonts.googleapis.com/css2?family=Josefin+Sans:wght@200;300&family=Roboto:wght@400&display=swap" rel="stylesheet">
<style>
  :root {
    --page: #5f5f61;
    --panel: #87888a;
    --header: #fdfdfd;
    --brand: #f15a29;
    --ink: #ffffff;
    --logo-ink: #3a3a3c;
  }
  * { margin: 0; padding: 0; box-sizing: border-box; }
  html, body { width: 1200px; height: 848px; overflow: hidden; }
  body { background: var(--page); position: relative; font-family: "Roboto", sans-serif; color: var(--ink); }

  .top-strip { position: absolute; left: 0; top: 0; width: 1200px; height: 16px; background: #ffffff; }
  .site-header { position: absolute; left: 0; top: 16px; width: 1200px; height: 140px; background: var(--header); box-shadow: 0 3px 6px rgba(0,0,0,.25); z-index: 2; }
  .brand { position: absolute; left: 60px; top: 44px; display: flex; align-items: center; gap: 12px; }
  .brand-mark { width: 52px; height: 52px; background: var(--brand); }
  .brand-name { font-family: "Roboto", sans-serif; font-weight: 400; color: var(--logo-ink); line-height: 1.1; }
  .brand-name .line-main { display: block; font-size: 28px; letter-spacing: -0.5px; }
  .brand-name .line-sub { display: block; font-size: 14px; letter-spacing: 0.5px; }

  .icon-panel { position: absolute; left: 15px; width: 1170px; background: var(--panel); }
  .icon-panel.row-one { top: 156px; height: 274px; }
  .icon-panel.row-two { top: 447px; height: 286px; }

  .service-icon { position: absolute; width: 61px; height: 61px; border-radius: 5px; background: var(--brand); display: flex; align-items: center; justify-content: center; }
  .service-icon svg { width: 40px; height: 40px; }

  .service-title { position: absolute; width: 360px; margin-left: -180px; text-align: center; font-family: "Josefin Sans", sans-serif; font-weight: 200; font-size: 40px; letter-spacing: 3px; line-height: 1; }
  .service-note { position: absolute; font-size: 26px; line-height: 25px; letter-spacing: 1.3px; white-space: nowrap; }
</style>
</head>
<body>
  <div class="top-strip"></div>
  <header class="site-header">
    <div class="brand">
      <span class="brand-mark"></span>
      <span class="brand-name"><span class="line-main">KEENRIDGE</span><span class="line-sub">GROWTH PARTNERS</span></span>
    </div>
  </header>

  <section class="icon-panel row-one"></section>
  <section class="icon-panel row-two"></section>

  <!-- Valuation -->
  <div class="service-icon" style="left:169px;top:191px">
    <svg viewBox="0 0 40 40" fill="none" stroke="#fff" stroke-width="2"><path d="M8 13 L20 19 L32 13 L32 28 L20 34 L8 28 Z" fill="#fff"/><path d="M20 19 V34" stroke="#f15a29"/><path d="M17 6 q3 -3 5 0 q-2 3 -5 4 h6" stroke-width="1.5"/></svg>
  </div>
  <div class="service-title" style="left:200px;top:288px">VALUATION</div>
  <div class="service-note" style="left:114px;top:342px">How to value<br>a business.</div>

  <!-- Advisory -->
  <div class="service-icon" style="left:538px;top:191px">
    <svg viewBox="0 0 40 40" fill="#fff"><rect x="4" y="5" width="24" height="17" rx="4"/><path d="M9 21 L8 28 L15 21 Z"/><rect x="16" y="17" width="21" height="14" rx="4"/><path d="M31 30 L33 36 L26 30 Z"/><path d="M8 10 H24 M8 14 H24 M8 18 H18" stroke="#f15a29" stroke-width="1.6"/></svg>
  </div>
  <div class="service-title" style="left:570px;top:288px">ADVISORY</div>
  <div class="service-note" style="left:434px;top:342px">Advising/ Consulting<br>with a business.</div>

  <!-- Survey -->
  <div class="service-icon" style="left:883px;top:191px">
    <svg viewBox="0 0 40 40" fill="#fff"><path d="M9 7 H26 L32 13 V34 H9 Z" opacity=".75"/><path d="M11 5 H27 L33 11 V32 H11 Z"/><path d="M27 5 V11 H33" fill="none" stroke="#f15a29" stroke-width="1.5"/></svg>
  </div>
  <div class="service-title" style="left:918px;top:288px">SURVEY</div>
  <div class="service-note" style="left:847px;top:342px">Reader survey<br>and responses.</div>

  <!-- Plan -->
  <div class="service-icon" style="left:169px;top:495px">
    <svg viewBox="0 0 40 40" fill="none" stroke="#fff" stroke-width="2"><rect x="4" y="5" width="32" height="21" fill="#fff"/><path d="M20 26 V36 M13 36 H27"/><path d="M9 21 Q16 11 22 17 T31 10" stroke="#f15a29" stroke-width="1.2" stroke-dasharray="2 1.5"/><circle cx="31" cy="10" r="1.3" fill="#f15a29" stroke="none"/></svg>
  </div>
  <div class="service-title" style="left:198px;top:584px">PLAN</div>
  <div class="service-note" style="left:110px;top:632px">Business Plan.</div>

  <!-- Launch -->
  <div class="service-icon" style="left:538px;top:495px">
    <svg viewBox="0 0 40 40" fill="none" stroke="#fff" stroke-width="2.2"><path d="M4 20 Q9 14 12 20 T18 12"/><path d="M36 20 Q31 14 28 20 T22 12"/><path d="M17 30 L22 14 M23 30 L18 14" stroke-width="1.8"/><circle cx="16" cy="32" r="2.5" stroke-width="1.6"/><circle cx="24" cy="32" r="2.5" stroke-width="1.6"/></svg>
  </div>
  <div class="service-title" style="left:570px;top:586px">LAUNCH</div>
  <div class="service-note" style="left:462px;top:636px">Launching a new<br>Business.</div>

  <!-- Video -->
  <div class="service-icon" style="left:884px;top:495px">
    <svg viewBox="0 0 40 40"><circle cx="20" cy="20" r="16" fill="#fff"/><path d="M16 12 L28 20 L16 28 Z" fill="#f15a29"/></svg>
  </div>
  <div class="service-title" style="left:917px;top:586px">VIDEO</div>
  <div class="service-note" style="left:821px;top:636px">Keenridge content<br>and feature videos.</div>
</body>
</html>
```